Startup Drone Platform Company business card

We are needing a business card design for our employees. We are a startup drone platform. We are looking for a business card that has our logo on one side, with the employee/company details on the opposite side. We are looking for something that is very eye catching, modern, and bold.

Target Market(s)

This will target both drone pilots and drone businesses, along with all the industries that could utilize drone services (aerial video, aerial photos, inspections, 3d mapping, etc).

Industry/Entity Type

Business

```html
<!DOCTYPE html>
<html lang="en">
<head>
<meta charset="utf-8">
<title>Rotor Lift — Business Card</title>
<link rel="stylesheet" href="https://fonts.googleapis.com/css2?family=Montserrat:wght@300;400;600&display=swap">
<style>
  :root {
    --stage: #3a3431;
    --card: #141516;
    --card-edge: #1d1e20;
    --white: #f2f2f2;
    --grey: #9a9a9a;
    --teal: #2fb3b8;
    --divider: #55585b;
  }
  * { margin: 0; padding: 0; box-sizing: border-box; }
  html, body { width: 1200px; height: 864px; overflow: hidden; }
  body {
    background: var(--stage);
    font-family: "Montserrat", Arial, sans-serif;
    color: var(--white);
    position: relative;
  }
  .card {
    position: absolute;
    width: 540px;
    height: 309px;
    background: var(--card);
    border: 1px solid var(--card-edge);
    border-radius: 3px;
    box-shadow: 0 10px 30px rgba(0,0,0,0.45);
  }
  .card--front { left: 45px; top: 140px; }
  .card--back { left: 615px; top: 415px; }

  /* Front */
  .brand-mark {
    position: absolute;
    left: 0; right: 0; top: 105px;
    display: flex; align-items: center; justify-content: center; gap: 14px;
  }
  .brand-mark__dot {
    width: 22px; height: 22px; border-radius: 50%;
    border: 4px solid var(--teal);
  }
  .brand-mark__name {
    font-weight: 300; font-size: 30px; letter-spacing: 10px;
    text-transform: uppercase; color: var(--white);
  }
  .front-url {
    position: absolute; left: 34px; bottom: 34px;
    font-size: 12px; letter-spacing: 6px; color: var(--grey);
  }

  /* Back */
  .wordmark {
    position: absolute; left: 0; right: 0; top: 58px;
    text-align: center;
    font-weight: 400; font-size: 25px; letter-spacing: 13px;
    text-transform: uppercase; color: var(--white);
  }
  .details {
    position: absolute; left: 0; right: 0; top: 140px;
    display: flex; justify-content: center;
  }
  .person {
    text-align: right; padding-right: 20px;
    font-size: 14px; line-height: 19px; color: var(--white);
  }
  .person__name { color: var(--teal); font-weight: 600; font-size: 17px; line-height: 22px; }
  .divider { width: 1px; background: var(--divider); height: 104px; }
  .contacts { list-style: none; padding-left: 20px; font-size: 14px; line-height: 23px; }
  .contacts li { display: flex; align-items: center; gap: 10px; }
  .contacts svg { width: 14px; height: 14px; fill: var(--teal); flex: none; }
</style>
</head>
<body>
  <section class="card card--front" aria-label="Card front">
    <div class="brand-mark">
      <span class="brand-mark__dot"></span>
      <span class="brand-mark__name">Rotor Lift</span>
    </div>
    <p class="front-url">www.rotorlift.com</p>
  </section>

  <section class="card card--back" aria-label="Card back">
    <h1 class="wordmark">Rotor Lift</h1>
    <div class="details">
      <div class="person">
        <p class="person__name">Mark Ellison</p>
        <p class="person__title">President</p>
        <p>2710 Harbor View Lane</p>
        <p>Mill Ridge, NY 10990</p>
      </div>
      <div class="divider"></div>
      <ul class="contacts">
        <li>
          <svg viewBox="0 0 16 16" aria-hidden="true"><path d="M3 1h3l1.5 4-2 1.2a9 9 0 0 0 4.3 4.3L11 8.5l4 1.5v3a2 2 0 0 1-2 2A12 12 0 0 1 1 3a2 2 0 0 1 2-2z"/></svg>
          <span>555 0147 8820</span>
        </li>
        <li>
          <svg viewBox="0 0 16 16" aria-hidden="true"><path d="M4 0h8a1 1 0 0 1 1 1v14a1 1 0 0 1-1 1H4a1 1 0 0 1-1-1V1a1 1 0 0 1 1-1zm1 2v10h6V2zm3 11a1 1 0 1 0 0 2 1 1 0 0 0 0-2z"/></svg>
          <span>555 0198 6412</span>
        </li>
        <li>
          <svg viewBox="0 0 16 16" aria-hidden="true"><path d="M4 0h8v5H4zM1 6h14v7h-3v3H4v-3H1zm4 5v3h6v-3z"/></svg>
          <span>555 0136 2075</span>
        </li>
        <li>
          <svg viewBox="0 0 16 16" aria-hidden="true"><path d="M0 3h16v1.2L8 9 0 4.2zM0 6l8 4.8L16 6v7H0z"/></svg>
          <span>mark@rotorlift.com</span>
        </li>
      </ul>
    </div>
  </section>
</body>
</html>
```